Wordpress Design for my Consulting Company

We want a WordPress site created for our new business. We have created a mock-up of the content we want on the site at https://marcusdellow.example-sites.com/website-5

We are not attached to any of the pictures and just put stock stuff from wix's editor, which we don't have rights to use outside of wix.

We are NOT looking to just port this site to WordPress, we are looking for some creative ways to display the content in a more professional artistic sense.

I have included several logo files and a text file with the colors and Fonts used in the logo. We are not looking to change the logo or the colors used in the logo.

The Schedule appointment links to a page that embeds a bookingnest.example.com calendar. https://bookingnest.example.com/marcus-dellow/brightvale

The final website domain will be enterprisebrightvale.example

Enterprise brightvale is a consulting company that works directly with the business owners and leaders of small businesses between 50-200 employees. We help companies make sure they have the right technology to meet their strategic goals. We are the anti-"Computer Guy" and we focus on business outcomes NOT cool technology gadgets.

The final design should communicate business growth and success.

Target Market(s)

Business Owners of companies with 50-200 employees

Coding

Coded - Design and coding required

Number of Pages Required

1 page

Font styles to use
Serif
Other font styles liked:
• Trajan Pro Bold, Open Sans

Requirements
Must have
• Should focus on consulting rather than technology.
• Should show the customer as the hero and we are just their guide.
• Must use the logo provided and the colors and fonts in the text file provided. Any other colors and fonts must be complementary.
• The design should scale for all devices computer, iPad, or phone
Should not have
• Should not focus on technology, we are the anti-"Computer Guy" and we focus on business outcomes NOT cool technology gadgets.

```html
<!DOCTYPE html>
<html lang="en">
<head>
<meta charset="utf-8">
<title>Enterprise Brightvale – Technology Advisors</title>
<link rel="stylesheet" href="https://fonts.googleapis.com/css2?family=Cinzel:wght@400;700&family=Open+Sans:wght@400;600;700&display=swap">
<style>
:root{
  --orange:#c0653a;
  --orange-dark:#9c4a26;
  --ink:#2e353b;
  --text:#4a4f54;
  --grey:#ececec;
  --grey-mid:#d9d9d9;
  --white:#ffffff;
  --brown:#2a1d16;
}
*{box-sizing:border-box;margin:0;padding:0}
html,body{width:1200px;height:5263px;overflow:hidden}
body{position:relative;background:var(--white);font-family:"Open Sans",Arial,sans-serif;color:var(--text)}
.abs{position:absolute}
.serif{font-family:"Cinzel",Georgia,serif}
.btn{position:absolute;background:var(--ink);color:var(--white);font-family:"Cinzel",Georgia,serif;font-weight:700;font-size:15px;letter-spacing:.5px;display:flex;align-items:center;justify-content:center;white-space:nowrap}
.btn--light{background:var(--white);color:var(--ink)}
/* header */
.site-header{position:absolute;left:0;top:0;width:1200px;height:95px;background:var(--white)}
.brand{position:absolute;left:140px;top:18px;display:flex;align-items:center;gap:12px}
.brand__mark{width:56px;height:56px;border-radius:50%;background:var(--ink);flex:none}
.brand__name{font-family:"Cinzel",Georgia,serif;font-size:15px;color:var(--ink);line-height:1.2;white-space:nowrap}
.brand__tag{font-family:"Cinzel",Georgia,serif;font-size:7px;color:var(--ink);white-space:nowrap}
.nav{position:absolute;top:42px;font-family:"Cinzel",Georgia,serif;font-size:13px;color:var(--ink);white-space:nowrap}
.nav--active{color:var(--orange)}
.nav-cta{position:absolute;left:888px;top:30px;width:166px;height:38px;border:1.5px solid var(--ink);font-family:"Cinzel",Georgia,serif;font-size:12px;color:var(--ink);display:flex;align-items:center;justify-content:center;white-space:nowrap}
/* hero */
.hero-photo{position:absolute;left:0;top:95px;width:1200px;height:625px;background:radial-gradient(ellipse at 48% 40%,#f4f5f6 0%,#d7d9db 55%,#b8bcbf 100%)}
.hero-title{position:absolute;left:144px;top:268px;font-size:25px;font-weight:600;color:var(--ink);line-height:1.3}
.hero-arrow{position:absolute;top:310px;width:36px;height:36px;border-radius:50%;background:var(--orange)}
/* steps */
.steps-title{position:absolute;left:144px;top:790px;font-size:33px;font-weight:700;color:var(--orange);line-height:1.2;white-space:nowrap}
.step-card{position:absolute;width:380px;height:110px;background:var(--white);box-shadow:0 4px 14px rgba(0,0,0,.22);display:flex;align-items:center;padding:0 16px}
.step-card__icon{width:80px;height:80px;flex:none;display:flex;align-items:center;justify-content:center;border-right:1px solid var(--grey-mid);margin-right:16px}
.step-card__name{font-family:"Cinzel",Georgia,serif;font-size:18px;color:var(--ink);margin-bottom:6px}
.step-card__text{font-size:10px;line-height:1.4;color:var(--text)}
/* sections */
.body-copy{font-size:16px;line-height:1.55}
.section-title{position:absolute;left:0;width:1200px;text-align:center;font-family:"Cinzel",Georgia,serif;font-weight:700;color:var(--orange)}
.panel{position:absolute;background:var(--grey);box-shadow:0 3px 12px rgba(0,0,0,.15)}
.tick-list{list-style:none}
.tick-list li{display:flex;gap:14px;font-size:14.5px;line-height:1.45;margin-bottom:20px}
.tick-list svg{flex:none;margin-top:3px}
.photo{position:absolute}
.quote{position:absolute;left:130px;width:940px;top:3025px;text-align:center;font-size:23px;line-height:1.5;color:var(--ink)}
.dot{position:absolute;top:3183px;width:11px;height:11px;border-radius:50%;background:var(--grey-mid)}
/* footer */
.contact-line{position:absolute;left:0;width:1200px;text-align:center;font-size:15px;color:var(--white)}
.field{position:absolute;border:1px solid #8e969c;color:var(--white);font-size:12px;padding:8px 10px;background:transparent}
.foot-links{position:absolute;left:144px;top:5172px;font-size:12px;color:var(--ink)}
.foot-copy{position:absolute;left:144px;top:5203px;font-size:11px;color:var(--text)}
</style>
</head>
<body>

<!-- header -->
<header class="site-header">
  <div class="brand">
    <div class="brand__mark"></div>
    <div>
      <div class="brand__name">Enterprise Brightvale</div>
      <div class="brand__tag">Strategic Technology Business Guide</div>
    </div>
  </div>
  <span class="nav nav--active" style="left:447px">Home</span>
  <span class="nav" style="left:517px">About Us</span>
  <span class="nav" style="left:612px">Services</span>
  <span class="nav" style="left:700px">Reviews</span>
  <span class="nav" style="left:786px">Contact Us</span>
  <span class="nav-cta">Schedule Appointment</span>
</header>

<!-- hero -->
<div class="hero-photo" role="img" aria-label="Open hand holding a floating silver compass with red and blue needles over a pale world map"></div>
<div class="hero-title">Technology Advisors<br>That “Get” Business.</div>
<div class="hero-arrow" style="left:44px"><svg width="36" height="36"><path d="M21 11l-7 7 7 7" stroke="#fff" stroke-width="3" fill="none"/></svg></div>
<div class="hero-arrow" style="left:1118px"><svg width="36" height="36"><path d="M15 11l7 7-7 7" stroke="#fff" stroke-width="3" fill="none"/></svg></div>
<svg class="abs" style="left:0;top:540px" width="1200" height="200">
  <polygon points="0,180 1200,30 1200,200 0,200" fill="var(--white)"/>
  <polygon points="500,118 1200,20 1200,44" fill="var(--orange)"/>
</svg>

<!-- four steps -->
<h2 class="steps-title serif">The Four Steps to<br>Aligning Technology<br>to your Business Strategy!</h2>

<div class="step-card" style="left:674px;top:797px">
  <div class="step-card__icon"><svg width="44" height="44"><circle cx="18" cy="18" r="12" stroke="#555" stroke-width="3" fill="none"/><path d="M27 27l12 12" stroke="#555" stroke-width="5"/></svg></div>
  <div><div class="step-card__name">Discover</div><div class="step-card__text">Identify what is going on behind the scenes and create a snapshot of current infrastructure.</div></div>
</div>
<div class="step-card" style="left:579px;top:930px">
  <div class="step-card__icon"><svg width="44" height="44" fill="none" stroke="#555" stroke-width="2.5"><circle cx="22" cy="12" r="6"/><path d="M10 36c0-9 5-14 12-14s12 5 12 14"/><circle cx="8" cy="16" r="4"/><circle cx="36" cy="16" r="4"/></svg></div>
  <div><div class="step-card__name">Prioritize</div><div class="step-card__text">Meet to decide which solutions and policies will have the greatest impact on reaching your goals.</div></div>
</div>
<div class="step-card" style="left:481px;top:1053px">
  <div class="step-card__icon"><svg width="44" height="44" fill="none" stroke="#555" stroke-width="3"><circle cx="22" cy="22" r="7"/><circle cx="22" cy="22" r="15" stroke-dasharray="6 4"/></svg></div>
  <div><div class="step-card__name">Implement</div><div class="step-card__text">Implement those things that will give the greatest return on investment.</div></div>
</div>
<div class="step-card" style="left:386px;top:1183px">
  <div class="step-card__icon"><svg width="44" height="44"><path d="M8 36l18-18" stroke="#555" stroke-width="5"/><circle cx="31" cy="13" r="8" fill="none" stroke="#555" stroke-width="3"/></svg></div>
  <div><div class="step-card__name">Maintain</div><div class="step-card__text">Create a system that keeps your technology aligned as strategy adjusts over time.</div></div>
</div>

<!-- lightbulb band -->
<svg class="abs" style="left:0;top:1370px" width="1200" height="640" role="img" aria-label="Businessman standing in a lightbulb-shaped doorway looking out at a city skyline">
  <defs>
    <radialGradient id="bulbGlow" cx="52%" cy="48%" r="45%">
      <stop offset="0" stop-color="#e9e4dc"/><stop offset=".45" stop-color="#b59c82"/><stop offset="1" stop-color="#2a1d16"/>
    </radialGradient>
  </defs>
  <polygon points="0,140 1200,6 1200,505 0,630" fill="url(#bulbGlow)"/>
  <polygon points="0,136 1200,2 1200,10 0,146" fill="var(--ink)"/>
  <polygon points="0,625 1200,500 1200,510 0,636" fill="var(--orange)"/>
</svg>
<p class="abs body-copy" style="left:144px;top:1612px;width:290px;color:#fff;font-size:14.5px">Computer guys frustrate business leaders because they don't have a business mindset. Brightvale advises on strategy that helps companies apply technology to gain a competitive advantage.</p>
<div class="btn btn--light" style="left:144px;top:1800px;width:216px;height:36px;font-size:13px">Schedule Appointment</div>

<!-- computer guys -->
<h2 class="section-title" style="top:2065px;font-size:33px">Are you tired of “Computer Guys” that…</h2>
<div class="photo" style="left:568px;top:2133px;width:485px;height:457px;background:linear-gradient(135deg,#5b6a72,#a8a39a 50%,#3b3f42)" role="img" aria-label="Colleagues in a bright office discussing ideas around a table"></div>
<div class="panel" style="left:144px;top:2165px;width:488px;height:460px;padding:40px 36px 0 36px">
  <ul class="tick-list">
    <li><svg width="16" height="16"><circle cx="8" cy="8" r="8" fill="#555"/><path d="M4 8l3 3 5-6" stroke="#fff" stroke-width="2" fill="none"/></svg>Don't want to be involved in business strategy.</li>
    <li><svg width="16" height="16"><circle cx="8" cy="8" r="8" fill="#555"/><path d="M4 8l3 3 5-6" stroke="#fff" stroke-width="2" fill="none"/></svg>Give you the excuse, “You never asked.”</li>
    <li><svg width="16" height="16"><circle cx="8" cy="8" r="8" fill="#555"/><path d="M4 8l3 3 5-6" stroke="#fff" stroke-width="2" fill="none"/></svg>Say “No!” but do not give options on how to achieve your business outcome.</li>
    <li><svg width="16" height="16"><circle cx="8" cy="8" r="8" fill="#555"/><path d="M4 8l3 3 5-6" stroke="#fff" stroke-width="2" fill="none"/></svg>Recommend technology when a simple process or policy change would have the same effect.</li>
    <li><svg width="16" height="16"><circle cx="8" cy="8" r="8" fill="#555"/><path d="M4 8l3 3 5-6" stroke="#fff" stroke-width="2" fill="none"/></svg>Can't explain how a technology will create business value, but insist it is necessary.</li>
    <li><svg width="16" height="16"><circle cx="8" cy="8" r="8" fill="#555"/><path d="M4 8l3 3 5-6" stroke="#fff" stroke-width="2" fill="none"/></svg>Suggest expensive solutions that are just thrown away, soon after they are deployed.</li>
  </ul>
</div>
<div class="btn" style="left:281px;top:2602px;width:214px;height:38px;font-size:13px">Schedule Appointment</div>

<!-- testimonial -->
<svg class="abs" style="left:0;top:2710px" width="1200" height="640">
  <polygon points="0,190 1200,10 1200,470 0,625" fill="var(--grey)"/>
  <polygon points="0,186 1200,6 1200,14 0,196" fill="var(--ink)"/>
  <polygon points="0,620 1200,465 1200,478 0,634" fill="var(--orange)"/>
</svg>
<div class="photo" style="left:551px;top:2870px;width:98px;height:96px;background:linear-gradient(#c7b9a8,#4a4540)" role="img" aria-label="Portrait of the client"></div>
<div class="abs" style="left:0;width:1200px;top:2982px;text-align:center;font-size:20px;color:var(--orange)">-Dana Whitfield, Print Harbor</div>
<p class="quote">"I knew I was behind, I just didn't know by how much.  We had years of band-aided solutions and Brightvale helped us stabilize our environment and position ourselves to compete in the quickly changing world of copy and print"</p>
<span class="dot" style="left:556px;background:var(--orange)"></span>
<span class="dot" style="left:580px"></span>
<span class="dot" style="left:604px"></span>
<span class="dot" style="left:628px"></span>

<!-- discovery -->
<h2 class="section-title" style="top:3418px;font-size:33px;line-height:1.2">A Discovery Process To<br>Achieve Your Business Goals</h2>
<div class="photo" style="left:144px;top:3520px;width:488px;height:456px;background:linear-gradient(120deg,#d9a46a,#f2e3b0 45%,#7c8a93)" role="img" aria-label="Team planning with colourful sticky notes on a glass wall"></div>
<div class="panel" style="left:579px;top:3551px;width:474px;height:450px;padding:26px 30px 0 30px">
  <p style="font-size:13px;line-height:1.5;margin-bottom:20px">We get the frustration of working with consultants and experts who don't listen or take the time to understand your company goals and vision. We believe technology should serve your business, not the other way around.</p>
  <ul class="tick-list">
    <li><svg width="16" height="16"><circle cx="8" cy="8" r="8" fill="#555"/><path d="M4 8l3 3 5-6" stroke="#fff" stroke-width="2" fill="none"/></svg>We Get… Scaling Up</li>
    <li><svg width="16" height="16"><circle cx="8" cy="8" r="8" fill="#555"/><path d="M4 8l3 3 5-6" stroke="#fff" stroke-width="2" fill="none"/></svg>We Get… Eliminating Bottlenecks</li>
    <li><svg width="16" height="16"><circle cx="8" cy="8" r="8" fill="#555"/><path d="M4 8l3 3 5-6" stroke="#fff" stroke-width="2" fill="none"/></svg>We Get… Preparing for Disruption</li>
    <li><svg width="16" height="16"><circle cx="8" cy="8" r="8" fill="#555"/><path d="M4 8l3 3 5-6" stroke="#fff" stroke-width="2" fill="none"/></svg>We Get… Reducing time to Decision</li>
    <li><svg width="16" height="16"><circle cx="8" cy="8" r="8" fill="#555"/><path d="M4 8l3 3 5-6" stroke="#fff" stroke-width="2" fill="none"/></svg>We Get… Leverage</li>
    <li><svg width="16" height="16"><circle cx="8" cy="8" r="8" fill="#555"/><path d="M4 8l3 3 5-6" stroke="#fff" stroke-width="2" fill="none"/></svg>We Get… Standardizing Customer Experience</li>
  </ul>
</div>
<div class="btn" style="left:702px;top:3988px;width:216px;height:38px;font-size:13px">Schedule Appointment</div>

<!-- footer contact -->
<svg class="abs" style="left:0;top:4110px" width="1200" height="960">
  <polygon points="0,140 1200,10 1200,895 0,955" fill="var(--ink)"/>
  <polygon points="200,118 1200,8 1200,20" fill="var(--orange)"/>
  <polygon points="0,950 1200,888 1200,900 0,960" fill="var(--orange)"/>
</svg>
<h2 class="section-title" style="top:4336px;font-size:36px;color:var(--white);font-weight:400">Contact Us</h2>
<div class="contact-line" style="top:4396px">&#9679; 1480 Meridian Parkway, Suite 310 Fairhaven, TX 77990</div>
<div class="contact-line" style="top:4428px">&#9993; mdellow@enterprisebrightvale.example</div>
<div class="contact-line" style="top:4460px">&#9742; (555) 014-2290</div>
<div class="abs" style="left:144px;top:4516px;width:909px;height:1px;background:#6d757b"></div>
<h2 class="section-title" style="top:4552px;font-size:32px;color:var(--white);font-weight:400">Schedule Appointment</h2>
<div class="field" style="left:144px;top:4618px;width:219px;height:40px">Name</div>
<div class="field" style="left:374px;top:4618px;width:219px;height:40px">Email</div>
<div class="field" style="left:604px;top:4618px;width:219px;height:40px">Phone</div>
<div class="field" style="left:834px;top:4618px;width:219px;height:40px">Subject</div>
<div class="field" style="left:144px;top:4674px;width:909px;height:40px">Address</div>
<div class="field" style="left:144px;top:4732px;width:909px;height:128px">Message</div>
<div class="btn" style="left:551px;top:4880px;width:98px;height:38px;background:var(--orange);font-size:14px">Submit</div>

<!-- bottom bar -->
<div class="foot-links">Home &nbsp;|&nbsp; About Us &nbsp;|&nbsp; Services &nbsp;|&nbsp; Reviews &nbsp;|&nbsp; Contact Us &nbsp;|&nbsp; Schedule Appointment</div>
<div class="foot-copy">Copyright © 2018. Enterprise Brightvale - All rights reserved.</div>
<span class="abs" style="left:1002px;top:5190px;width:14px;height:14px;border-radius:50%;background:var(--ink)"></span>
<span class="abs" style="left:1030px;top:5190px;width:14px;height:14px;border-radius:50%;background:var(--ink)"></span>

</body>
</html>
```